Flyer for a conference next week

We need a flyer to promote our stand at a conference next week - involving a Pebble Jar Contest.

The following files are attached:

- Existing Company Logos
- The logo of the product we are promoting (oVerla)
- A previous flyer - may be useful
- a Jellybean image (we want this to be the major part of the design

The flyer will be size : DL - 109mm x 220mm (5mm bleed) and 300 DPI

The flyer should include the following text :

"Take the Pebble Jar Contest at the Tallow Reef table in the exhibit space and win a Drone!"

"Find out more about our oVerla Web Services platform for Financial Models"

Colors
ed2e35

Requirements
Must have
• The flyer will be size : DL - 109mm x 220mm (5mm bleed) and 300 DPI
• The flyer should include the following text :
• "Take the Pebble Jar Contest at the Tallow Reef table in the exhibit space and win a Drone!"
• "Find out more about our oVerla Web Services platform for Financial Models"

```html
<!DOCTYPE html>
<html lang="en">
<head>
<meta charset="utf-8">
<title>oVerla – Pebble Jar Contest Flyer</title>
<link rel="stylesheet" href="https://fonts.googleapis.com/css2?family=Jost:ital,wght@0,400;0,500;0,600;0,700;0,800;1,500&display=swap">
<style>
  :root {
    --stage: #e4e4e4;
    --deep-red: #6e0509;
    --dark-red: #8e0d12;
    --brand-red: #ed2e35;
    --mid-red: #d9262d;
    --white: #ffffff;
    --ink: #1d1d1d;
  }
  * { margin: 0; padding: 0; box-sizing: border-box; }
  html, body { width: 870px; height: 1200px; overflow: hidden; }
  body { background: var(--stage); font-family: "Jost", sans-serif; position: relative; }

  .flyer {
    position: absolute; left: 152px; top: 30px;
    width: 566px; height: 1140px; overflow: hidden;
    background: var(--dark-red);
  }
  .flyer-shapes { position: absolute; inset: 0; }

  .brand { position: absolute; left: 32px; top: 44px; color: var(--white); }
  .brand-name { font-size: 54px; font-weight: 500; letter-spacing: 0.5px; line-height: 1; }
  .brand-url { font-size: 13px; margin-top: 14px; margin-left: 32px; }

  .headline {
    position: absolute; left: 0; top: 528px; width: 566px;
    transform: rotate(-5deg); transform-origin: 283px 140px;
    color: var(--white); font-weight: 800;
  }
  .headline-row { display: flex; align-items: flex-end; white-space: nowrap; }
  .row-take { padding-left: 100px; height: 62px; }
  .row-contest { padding-left: 34px; margin-top: 2px; }
  .row-table { padding-left: 60px; margin-top: 8px; }
  .row-exhibit { padding-left: 76px; margin-top: 6px; }
  .row-win { padding-left: 58px; margin-top: -4px; }

  .quote-mark { font-family: Georgia, serif; font-size: 104px; line-height: 1; font-weight: 700; }
  .quote-open { height: 62px; margin-right: 6px; }
  .quote-close { position: relative; top: -22px; margin-left: 4px; height: 60px; }
  .take-the { font-size: 38px; line-height: 1; padding-bottom: 4px; }
  .tag-box { background: var(--white); color: var(--ink); padding: 2px 14px; line-height: 1.15; }
  .contest-name { font-size: 44px; letter-spacing: -1px; }
  .contest-word { font-size: 22px; font-weight: 700; margin-left: 6px; padding-bottom: 10px; line-height: 1; }
  .at-the { font-size: 26px; margin-right: 10px; padding-bottom: 8px; line-height: 1; }
  .table-name { font-size: 34px; }
  .exhibit-line { font-size: 22px; font-weight: 700; line-height: 1.1; }
  .win-line { font-size: 56px; font-weight: 800; letter-spacing: 0.5px; line-height: 1; }

  .drone-photo { position: absolute; left: 120px; top: 828px; width: 330px; height: 118px; }

  .platform-note {
    position: absolute; left: 0; width: 566px; top: 958px;
    transform: rotate(-5deg); text-align: center;
    color: var(--white); font-style: italic; font-weight: 500; font-size: 21px; line-height: 1.25;
  }

  .footer { position: absolute; left: 56px; top: 1066px; display: flex; align-items: center; color: var(--white); }
  .footer-mark { width: 48px; height: 48px; border: 3px solid var(--white); border-radius: 50%; margin-right: 10px; }
  .footer-program { font-size: 9px; font-weight: 600; letter-spacing: 0.3px; }
  .footer-company { font-size: 21px; font-weight: 600; line-height: 1; }
  .footer-contact { margin-left: 18px; font-size: 11px; line-height: 1.4; font-weight: 400; }
</style>
</head>
<body>
  <article class="flyer">
    <svg class="flyer-shapes" width="566" height="1140" viewBox="0 0 566 1140">
      <defs>
        <linearGradient id="topBand" x1="0" y1="0" x2="1" y2="1">
          <stop offset="0" stop-color="#9c1116"/>
          <stop offset="1" stop-color="#5e0306"/>
        </linearGradient>
        <linearGradient id="bottomBand" x1="0" y1="0" x2="0" y2="1">
          <stop offset="0" stop-color="#7a070c"/>
          <stop offset="1" stop-color="#a0151b"/>
        </linearGradient>
        <linearGradient id="pebbles" x1="0" y1="0" x2="1" y2="1">
          <stop offset="0" stop-color="#f4c531"/>
          <stop offset="0.3" stop-color="#e8485f"/>
          <stop offset="0.55" stop-color="#4fa8dc"/>
          <stop offset="0.8" stop-color="#7bc24a"/>
          <stop offset="1" stop-color="#f08a2c"/>
        </linearGradient>
      </defs>
      <rect class="band-top" width="566" height="1140" fill="url(#topBand)"/>
      <polygon class="band-bottom" points="0,895 566,834 566,1140 0,1140" fill="url(#bottomBand)"/>
      <polygon class="band-middle" role="img" aria-label="Faint close-up of red candy beans" points="0,188 566,142 566,834 0,895" fill="var(--mid-red)"/>
      <line x1="566" y1="30" x2="80" y2="1140" stroke="#f59a8f" stroke-width="1.5" stroke-dasharray="2 5" opacity="0.5"/>
      <path class="pebble-photo" role="img" aria-label="Heap of colourful candy beans filling a bean-shaped window"
        d="M150,200 C230,168 360,172 430,250 C490,320 495,440 465,520 C440,580 380,605 320,595 C250,583 195,540 180,470 C170,420 200,380 188,320 C178,270 120,225 150,200 Z"
        fill="url(#pebbles)"/>
      <path class="pebble-outline" fill="none" stroke="var(--white)" stroke-width="3" stroke-dasharray="8 5"
        transform="translate(320 390) scale(1.05) translate(-320 -390)"
        d="M150,200 C230,168 360,172 430,250 C490,320 495,440 465,520 C440,580 380,605 320,595 C250,583 195,540 180,470 C170,420 200,380 188,320 C178,270 120,225 150,200 Z"/>
    </svg>

    <header class="brand">
      <div class="brand-name">oVerla</div>
      <div class="brand-url">www.tallowreef.com.au</div>
    </header>

    <div class="headline">
      <div class="headline-row row-take">
        <span class="quote-mark quote-open">&ldquo;</span>
        <span class="take-the">Take the</span>
      </div>
      <div class="headline-row row-contest">
        <span class="contest-name tag-box">PEBBLE JAR</span>
        <span class="contest-word">Contest</span>
      </div>
      <div class="headline-row row-table">
        <span class="at-the">at the</span>
        <span class="table-name tag-box">Tallow Reef table</span>
      </div>
      <div class="headline-row row-exhibit">
        <span class="exhibit-line">in the exhibit space and</span>
      </div>
      <div class="headline-row row-win">
        <span class="win-line">WIN A DRONE!</span>
        <span class="quote-mark quote-close">&rdquo;</span>
      </div>
    </div>

    <svg class="drone-photo" viewBox="0 0 330 118" role="img" aria-label="White camera drone in flight">
      <ellipse cx="165" cy="59" rx="160" ry="50" fill="#b8898b" opacity="0.55"/>
    </svg>

    <p class="platform-note">"Find out more about our oVerla Web Services<br>platform for Financial Models"</p>

    <footer class="footer">
      <div class="footer-mark"></div>
      <div class="footer-brand">
        <div class="footer-program">A PROGRAM FROM</div>
        <div class="footer-company">Tallow Reef</div>
      </div>
      <div class="footer-contact">For more information please contact us at :<br>overla@tallowreef.com.au</div>
    </footer>
  </article>
</body>
</html>
```